Akademie für Lichtwegkunde
Zielgruppe
Ich biete die beiden Seminare 'Kraftquell am Werktag' und 'Feinsinn am Werktag' an. Die Zielgruppe sind spirituell interessierte Leute.
Aufgabenstellung
Die Anzeige sollte mehr oder weniger mit den Farben meiner Webseite übereinstimmen (www.sonnenpfad-raum.ch).
Grösse der Anzeige:
breit: 121mm
hoch: 124mm
Die Anzeige sollte mein persönliches Bild und das Logo enthalten.
Text:
Feinsinn am Werktag:
Seminare zur Förderung Ihrer Intuition. Entdecken Sie Ihre eigene Medialität und lernen Sie diese gezielt im Alltag einzusetzen.
26./27. August 2017
11./12. November 2017
Kraftquell am Werktag:
Seminare für energetisches Heilen. Lernen Sie sich und andere Menschen energetisch zu begleiten.
16./17. September 2017
9./10. Dezember 2017
2 für 1 - Aktion:
Kommen Sie zu zweit und bezahlen Sie nur für eine Person
(gültig bis Ende 2017)
Webseite:
www.sonnenpfad-raum.ch
Seminarort: Grünholdau, 3286 Lorbachtal, Schweiz

```html
<!DOCTYPE html>
<html lang="de">
<head>
<meta charset="utf-8">
<title>Anzeige – Akademie für Lichtwegkunde</title>
<link href="https://fonts.googleapis.com/css2?family=Open+Sans:wght@400;600;700&display=swap" rel="stylesheet">
<style>
  :root {
    --stage: #d9d9d9;
    --paper: #ffffff;
    --ink: #2a2a2a;
    --ink-soft: #3a3a3a;
    --brand-blue: #2f86c6;
    --box-blue: rgba(32, 120, 190, 0.82);
    --box-orange: rgba(206, 112, 38, 0.86);
    --box-text: #ffffff;
  }
  * { margin: 0; padding: 0; box-sizing: border-box; }
  html, body {
    width: 1200px; height: 801px; overflow: hidden;
    background: var(--stage);
    font-family: "Open Sans", Arial, sans-serif;
  }
  .ad {
    position: absolute; left: 229px; top: 20px;
    width: 741px; height: 760px;
    background: var(--paper);
    color: var(--ink);
  }
  .ad-header { position: relative; height: 193px; }
  .offer { position: absolute; left: 36px; top: 30px; }
  .offer-kicker { font-size: 25px; font-weight: 400; line-height: 1.2; }
  .offer-headline { font-size: 32px; font-weight: 600; line-height: 1.16; margin-top: 2px; }
  .offer-validity { font-size: 15px; margin-top: 10px; }
  .brand {
    position: absolute; right: 40px; top: 62px;
    display: flex; align-items: center; gap: 14px;
  }
  .brand-dot { width: 30px; height: 30px; border-radius: 50%; background: var(--brand-blue); }
  .brand-name { font-size: 24px; font-weight: 600; color: var(--brand-blue); line-height: 1.15; width: 230px; }

  .seminar-band {
    position: relative; height: 371px;
  }
  .band-backdrop {
    position: absolute; inset: 0;
    background: linear-gradient(180deg, #7fa7cf 0%, #b9cde0 30%, #6f7a80 52%, #8fa6b8 62%, #b7cadb 78%, #6d8aa3 100%);
  }
  .seminar {
    position: absolute; top: 37px; width: 316px; height: 300px;
    padding: 14px 0 0 18px; color: var(--box-text);
  }
  .seminar--intuition { left: 35px; background: var(--box-blue); }
  .seminar--healing { left: 389px; background: var(--box-orange); }
  .seminar-label { font-size: 21px; line-height: 1.3; }
  .seminar-title { font-size: 24px; font-weight: 600; line-height: 1.25; }
  .seminar-text { font-size: 20px; line-height: 1.35; margin-top: 22px; }
  .seminar-dates { font-size: 20px; line-height: 1.3; margin-top: 24px; }

  .ad-footer { position: relative; height: 196px; }
  .portrait {
    position: absolute; left: 0; top: 0; width: 217px; height: 196px;
    background: linear-gradient(135deg, #cfcfcf 0%, #8a8a8a 55%, #4a4a4a 100%);
  }
  .contact { position: absolute; left: 252px; top: 36px; color: var(--ink-soft); }
  .contact-name { font-size: 22px; font-weight: 600; margin-bottom: 22px; }
  .contact-line { font-size: 17.5px; line-height: 1.36; }
</style>
</head>
<body>
  <article class="ad">
    <header class="ad-header">
      <div class="offer">
        <p class="offer-kicker">Aktion 2 für 1</p>
        <h1 class="offer-headline">Zu zweit kommen,<br>nur 1x bezahlen</h1>
        <p class="offer-validity">gültig bis 31.12.2017</p>
      </div>
      <div class="brand">
        <span class="brand-dot"></span>
        <span class="brand-name">Akademie für Lichtwegkunde</span>
      </div>
    </header>

    <section class="seminar-band">
      <div class="band-backdrop" role="img" aria-label="Bergsee mit Gipfeln, die sich im Wasser spiegeln, unter blauem Himmel"></div>
      <div class="seminar seminar--intuition">
        <p class="seminar-label">Feinsinn am Werktag</p>
        <h2 class="seminar-title">Seminar zur Förderung<br>Ihrer Intuition</h2>
        <p class="seminar-text">Entdecken Sie Ihre eigene Medialität und lernen Sie diese gezielt im Alltag einzusetzen.</p>
        <p class="seminar-dates">26. bis 27. August 2017<br>11. bis 12. November 2017</p>
      </div>
      <div class="seminar seminar--healing">
        <p class="seminar-label">Kraftquell am Werktag</p>
        <h2 class="seminar-title">Seminar für<br>energetisches Heilen</h2>
        <p class="seminar-text">Lernen Sie sich und andere Menschen energetisch zu begleiten.</p>
        <p class="seminar-dates">16. bis 17. September 2017<br>9. bis 10. Dezember 2017</p>
      </div>
    </section>

    <footer class="ad-footer">
      <div class="portrait" role="img" aria-label="Schwarzweiss-Porträt des Seminarleiters"></div>
      <div class="contact">
        <p class="contact-name">Lukas Bernthaler</p>
        <p class="contact-line">Lindenmattweg 7 · 3294 Feldwilen · T +41 (0)31 555 27 48</p>
        <p class="contact-line">info@sonnenpfad-raum.ch · www.sonnenpfad-raum.ch</p>
        <p class="contact-line">Seminarort: Grünholdau · 3286 Lorbachtal · Schweiz</p>
      </div>
    </footer>
  </article>
</body>
</html>
```